Dog treat Package Design

We’re looking for a creative and professional designer to develop eye-catching packaging for our upcoming line of premium dog treats under the Tailor Munch brand.
The design should reflect quality, trust, and natural nutrition, appealing to dog owners who value healthy, high-end pet products.
What We Need
Full packaging design for a resealable stand-up pouch (approx. 130 × 210 + 60 mm)
Front and back layout including space for logo, product name, ingredients, nutrition panel, barcode, and storage instructions
Print-ready files (with dielines, bleeds, and crop marks)
Editable source file (AI / PSD preferred)
3D mock-up or realistic rendering for presentation
Design Direction
Clean, minimal, and modern look with a premium feel
Use natural tones (e.g. earthy browns, creams, muted greens, or soft neutrals)
Should convey trust, wellness, and craftsmanship
Incorporate subtle texture or illustration that hints at natural ingredients or happy, healthy dogs
Must be consistent across potential product variations (e.g. chicken, beef, lamb treats)
Target Audience
Pet owners who value nutrition, quality ingredients, and design aesthetics — typically aged 25–50, with a focus on healthy, Australian-made pet products.
Deliverables
2 initial design concepts
Up to 2 revision rounds
Final deliverables in:
Print-ready PDF (CMYK)
Editable AI/PSD
High-resolution mock-ups
Design style similar to Fennel Paws
Target Market(s)
People with pets - Premium
Look and feel
Each slider illustrates characteristics of the customer's brand and the style your logo design should communicate.

```html
<!DOCTYPE html>
<html lang="en">
<head>
<meta charset="utf-8">
<title>Tailor Munch — Chicken Jerky Pouch</title>
<link rel="stylesheet" href="https://fonts.googleapis.com/css2?family=Playfair+Display:wght@900&family=Poppins:wght@400;500;600&display=swap">
<style>
  :root {
    --bg: #dcdcdc;
    --lime: #b9d238;
    --lime-light: #cfe06a;
    --green-mid: #8dbb3c;
    --green-deep: #5f8f33;
    --mist: #b5acb3;
    --stone: #8a8188;
    --slate: #5c555b;
    --ink: #2f2c2e;
    --white: #f7f7f5;
    --jerky-a: #9c4f2a;
    --jerky-b: #c9784a;
  }
  html, body {
    margin: 0;
    padding: 0;
    width: 1200px;
    height: 1199px;
    overflow: hidden;
    background: var(--bg);
  }
  .canvas {
    position: relative;
    width: 1200px;
    height: 1199px;
  }
  .pouch {
    position: absolute;
    left: 300px;
    top: 120px;
    width: 600px;
    height: 960px;
  }
  .title {
    font-family: "Playfair Display", serif;
    font-weight: 900;
    font-size: 46px;
    fill: var(--ink);
    letter-spacing: 0.5px;
  }
  .brand-name {
    font-family: "Poppins", sans-serif;
    font-weight: 600;
    font-size: 15px;
    letter-spacing: 1.5px;
    fill: var(--ink);
  }
  .badge-text {
    font-family: "Poppins", sans-serif;
    font-weight: 600;
    font-size: 13px;
    letter-spacing: 2px;
    fill: var(--ink);
  }
  .claim-label {
    font-family: "Poppins", sans-serif;
    font-size: 4.5px;
    font-weight: 500;
    fill: var(--ink);
  }
  .footer-text {
    font-family: "Poppins", sans-serif;
    font-size: 15px;
    fill: var(--white);
  }
  .icon-line {
    fill: none;
    stroke: var(--ink);
    stroke-width: 1.6;
    stroke-linecap: round;
    stroke-linejoin: round;
  }
</style>
</head>
<body>
<main class="canvas">
  <svg class="pouch" viewBox="0 0 600 960" xmlns="http://www.w3.org/2000/svg">
    <defs>
      <clipPath id="pouch-shape">
        <rect x="0" y="0" width="600" height="960" rx="18"/>
      </clipPath>
      <linearGradient id="jerky-fill" x1="0" y1="0" x2="1" y2="1">
        <stop offset="0" stop-color="var(--jerky-b)"/>
        <stop offset="0.5" stop-color="var(--jerky-a)"/>
        <stop offset="1" stop-color="#7a3c22"/>
      </linearGradient>
      <linearGradient id="foliage-fill" x1="1" y1="0" x2="0" y2="1">
        <stop offset="0" stop-color="#a9c63a"/>
        <stop offset="1" stop-color="var(--lime)" stop-opacity="0"/>
      </linearGradient>
      <path id="blob" d="M -1,-0.2 C -1,-0.7 -0.5,-0.9 -0.1,-0.75 C 0.3,-0.95 0.9,-0.8 0.95,-0.35 C 1.05,0.1 0.9,0.6 0.5,0.75 C 0.2,0.95 -0.2,0.8 -0.45,0.85 C -0.9,0.9 -1.05,0.35 -1,-0.2 Z"/>
      <path id="badge-arc-top" d="M 372,540 A 55,55 0 0 1 482,540"/>
      <path id="badge-arc-bottom" d="M 363,540 A 62,62 0 0 0 487,540"/>
    </defs>

    <g clip-path="url(#pouch-shape)">
      <rect class="pouch-base" width="600" height="960" fill="var(--lime)"/>

      <rect x="270" y="0" width="330" height="320" fill="url(#foliage-fill)" role="img" aria-label="Line illustration of leafy branches"/>

      <line x1="0" y1="100" x2="600" y2="100" stroke="#a6bf2e" stroke-width="3"/>

      <path d="M 0,440 C 60,400 120,460 160,420 L 600,400 L 600,960 L 0,960 Z" fill="var(--lime-light)" opacity="0.55"/>
      <path d="M 0,580 C 40,540 30,470 90,440 C 160,410 220,440 300,430 C 420,420 520,440 600,500 L 600,960 L 0,960 Z" fill="var(--green-mid)"/>
      <path d="M 0,840 C 80,820 120,900 220,880 C 320,860 380,920 470,890 C 530,870 570,900 600,890 L 600,960 L 0,960 Z" fill="var(--lime-light)"/>

      <use href="#blob" transform="translate(290,650) scale(320,250)" fill="var(--green-deep)" opacity="0.6"/>
      <use href="#blob" transform="translate(290,648) scale(285,222)" fill="var(--mist)"/>
      <use href="#blob" transform="translate(292,648) scale(245,192)" fill="var(--stone)"/>
      <use href="#blob" transform="translate(294,648) scale(210,165)" fill="var(--slate)"/>
      <use href="#blob" transform="translate(296,648) scale(178,140)" fill="var(--ink)"/>
      <use href="#blob" transform="translate(298,648) scale(158,122)" fill="url(#jerky-fill)" role="img" aria-label="Window showing chicken jerky strips"/>

      <path d="M 75,0 L 260,0 L 260,330 A 92.5,92.5 0 0 1 75,330 Z" fill="var(--white)"/>
      <text class="brand-name" x="167.5" y="345" text-anchor="middle">TAILOR MUNCH</text>

      <text class="title" x="300" y="300">CHICKEN</text>
      <text class="title" x="300" y="362">JERKY</text>

      <circle cx="427" cy="540" r="72" fill="var(--white)"/>
      <text class="badge-text"><textPath href="#badge-arc-top" startOffset="50%" text-anchor="middle">HIGH-QUALITY</textPath></text>
      <text class="badge-text"><textPath href="#badge-arc-bottom" startOffset="50%" text-anchor="middle">CHICKEN</textPath></text>
      <circle cx="427" cy="540" r="22" fill="var(--ink)" role="img" aria-label="Hen illustration"/>

      <g class="claims">
        <g transform="translate(118,820)">
          <circle r="22" fill="var(--white)"/>
          <text class="claim-label" y="-11" text-anchor="middle">100% NATURAL</text>
          <path class="icon-line" d="M 0,10 L 0,-2 M 0,2 C -8,2 -10,-4 -10,-7 C -4,-7 0,-4 0,2 M 0,2 C 8,2 10,-4 10,-7 C 4,-7 0,-4 0,2"/>
        </g>
        <g transform="translate(190,820)">
          <circle r="22" fill="var(--white)"/>
          <text class="claim-label" y="-11" text-anchor="middle">FREEZE DRIED</text>
          <path class="icon-line" d="M 0,-7 L 0,10 M -8,-3 L 8,6 M -8,6 L 8,-3"/>
        </g>
        <g transform="translate(260,820)">
          <circle r="22" fill="var(--white)"/>
          <text class="claim-label" y="-11" text-anchor="middle">100% MONO</text>
          <path class="icon-line" d="M -4,-6 C 6,-3 -6,3 4,10 M 4,-6 C -6,-3 6,3 -4,10"/>
        </g>
        <g transform="translate(332,820)">
          <circle r="22" fill="var(--white)"/>
          <text class="claim-label" y="-11" text-anchor="middle">WITHOUT</text>
          <path class="icon-line" d="M -3,-6 L -3,0 L -8,9 L 8,9 L 3,0 L 3,-6 M -9,-6 L 9,10"/>
        </g>
        <g transform="translate(404,820)">
          <circle r="22" fill="var(--white)"/>
          <text class="claim-label" y="-11" text-anchor="middle">HIGH PROTEIN</text>
          <path class="icon-line" d="M 0,-6 L -8,2 L -3,2 L -3,10 L 3,10 L 3,2 L 8,2 Z"/>
        </g>
        <g transform="translate(476,820)">
          <circle r="22" fill="var(--white)"/>
          <text class="claim-label" y="-11" text-anchor="middle">HIGH FLAVOR</text>
          <circle class="icon-line" cx="0" cy="3" r="8"/>
          <path class="icon-line" d="M -4,5 C -2,8 2,8 4,5"/>
        </g>
      </g>

      <text class="footer-text" x="100" y="878">FOR ALL LIFE STAGES</text>
      <text class="footer-text" x="490" y="876" text-anchor="end">NET WT. 120g</text>
    </g>
  </svg>
</main>
</body>
</html>
```